Mexican construction company needs a business card design

We need a business card design for a company based in Monterrey, Mexico called:

Desarrollos Tolvani S.A. de C.V.

The company is in the construction business and I would like the businees card to be simple and concise. Please use white background and blue or black text color that say:

"Proyectos de Construcción"-- (Brief description of business)
" Rodrigo Ulloa Benítez"--- (My name)
"rulloab@correovelo.mx"-- (My email)
"C: (81) 82 19 57 46"-- (My cell)
"O: (81) 86 72 13 95"-- (Office phone)

Please use only the colors of my company that are attached

Please make the back of the business card blue (same blue from logo) and use the logo.

Thanks!

```html
<!DOCTYPE html>
<html lang="es">
<head>
<meta charset="utf-8">
<title>Desarrollos Tolvani – Tarjeta de presentación</title>
<link href="https://fonts.googleapis.com/css2?family=Arimo:ital,wght@0,400;0,700;1,400&display=swap" rel="stylesheet">
<style>
  :root {
    --navy: #17154d;
    --navy-text: #1f1d5e;
    --tag-blue: #3b3a8f;
    --grey: #9b9b9f;
    --lavender: #5f5d98;
    --white: #ffffff;
    --sheet: #ffffff;
    --label: #222222;
  }
  * { box-sizing: border-box; margin: 0; padding: 0; }
  html, body {
    width: 1169px; height: 1200px; overflow: hidden;
    background: var(--sheet);
    font-family: "Arimo", Arial, sans-serif;
  }
  .sheet { position: relative; width: 1169px; height: 1200px; }
  .side-label {
    position: absolute; left: 0; width: 1169px; text-align: center;
    font-size: 30px; color: var(--label);
  }
  .side-label--front { top: 138px; }
  .side-label--back { top: 624px; }

  .card {
    position: absolute; left: 223px; width: 729px; height: 406px; overflow: hidden;
  }
  .card--front { top: 186px; background: var(--white); box-shadow: 0 0 0 1px #e4e4e8; }
  .card--back { top: 672px; background: var(--navy); }

  .company-name {
    position: absolute; left: 29px; top: 22px;
    font-size: 22px; font-weight: 700; color: var(--navy-text);
  }
  .brand-mark {
    position: absolute; display: flex; align-items: center; gap: 10px;
    font-weight: 700; letter-spacing: 0.5px;
  }
  .card--front .brand-mark {
    left: 50px; top: 172px; font-size: 36px; color: var(--navy);
  }
  .brand-mark__square { width: 22px; height: 22px; background: var(--grey); flex: none; }
  .tagline {
    position: absolute; left: 23px; width: 280px; top: 283px; text-align: center;
    font-size: 17px; color: var(--tag-blue);
  }
  .holder-name {
    position: absolute; left: 420px; top: 170px;
    font-size: 24px; color: var(--navy-text);
  }
  .contact-list { position: absolute; left: 420px; top: 276px; list-style: none; }
  .contact-list li {
    display: flex; align-items: center; gap: 12px; height: 33px;
    font-size: 15px; letter-spacing: 1.5px; color: var(--navy-text);
  }
  .contact-icon { width: 21px; height: 21px; flex: none; }
  .bar { position: absolute; }
  .card--front .bar--grey { left: 0; top: 383px; width: 134px; height: 23px; background: var(--grey); }
  .card--front .bar--navy { left: 140px; top: 383px; width: 589px; height: 23px; background: var(--navy); }

  .brand-watermark {
    position: absolute; left: -30px; top: 40px;
    font-size: 190px; font-weight: 700; color: var(--lavender);
    white-space: nowrap; line-height: 1;
  }
  .card--back .brand-mark {
    left: 520px; top: 170px; font-size: 38px; color: var(--white);
  }
  .card--back .bar--white { left: 0; top: 352px; width: 134px; height: 28px; background: var(--white); }
  .card--back .bar--grey {
    left: 143px; top: 352px; width: 586px; height: 28px; background: var(--grey);
    display: flex; align-items: center; justify-content: flex-end; padding-right: 18px;
    font-size: 16px; font-style: italic; color: var(--white);
  }
</style>
</head>
<body>
<div class="sheet">
  <div class="side-label side-label--front">Front</div>
  <section class="card card--front">
    <h1 class="company-name">Desarrollos Tolvani S.A. de C.V.</h1>
    <div class="brand-mark"><span class="brand-mark__square"></span>Tolvani</div>
    <p class="tagline">Proyectos de Construcción</p>
    <p class="holder-name">Rodrigo Ulloa Benítez</p>
    <ul class="contact-list">
      <li>
        <svg class="contact-icon" viewBox="0 0 20 20" aria-hidden="true">
          <circle cx="10" cy="10" r="10" fill="var(--navy)"/>
          <rect x="6.5" y="4" width="7" height="12" rx="1.5" fill="#fff"/>
          <rect x="7.7" y="5.5" width="4.6" height="7.5" fill="var(--navy)"/>
        </svg>
        <span>(81) 82 19 57 46</span>
      </li>
      <li>
        <svg class="contact-icon" viewBox="0 0 20 20" aria-hidden="true">
          <circle cx="10" cy="10" r="10" fill="var(--navy)"/>
          <path d="M6.2 4.8c.5-.4 1.2-.3 1.5.2l1.2 1.9c.3.5.2 1-.2 1.4l-.8.7c.6 1.4 1.7 2.5 3.1 3.1l.7-.8c.4-.4 1-.5 1.4-.2l1.9 1.2c.5.3.6 1 .2 1.5l-.9 1c-.6.6-1.5.8-2.3.5C8.7 14.3 5.7 11.3 4.7 8c-.3-.8-.1-1.7.5-2.3z" fill="#fff"/>
        </svg>
        <span>(81) 86 72 13 95</span>
      </li>
      <li>
        <svg class="contact-icon" viewBox="0 0 20 20" aria-hidden="true">
          <circle cx="10" cy="10" r="10" fill="var(--navy)"/>
          <circle cx="10" cy="10" r="2.3" fill="none" stroke="#fff" stroke-width="1.6"/>
          <path d="M12.3 8v2.8c0 1.3 2.3 1.3 2.3-.8a4.6 4.6 0 1 0-1.8 3.7" fill="none" stroke="#fff" stroke-width="1.6" stroke-linecap="round"/>
        </svg>
        <span>rulloab@correovelo.mx</span>
      </li>
    </ul>
    <div class="bar bar--grey"></div>
    <div class="bar bar--navy"></div>
  </section>

  <div class="side-label side-label--back">Back</div>
  <section class="card card--back">
    <div class="brand-watermark" aria-hidden="true">Tolvani</div>
    <div class="brand-mark"><span class="brand-mark__square"></span>Tolvani</div>
    <div class="bar bar--white"></div>
    <div class="bar bar--grey">Proyectos de Construcción</div>
  </section>
</div>
</body>
</html>
```